Small consulting business needs logo and business card design

I need a logo, business card and letterhead design for a small consulting firm called Veltramo Consulting. My customers are generally small to medium sized businesses but I have done work for major corporates and government departments. The field of consulting is strategic/business planning and program management. I have blue as the predominate colour in my current business card but I am happy to change this for the right design
Industry/Entity Type
Business

```html
<!DOCTYPE html>
<html lang="en">
<head>
<meta charset="utf-8">
<title>Veltramo Consulting — Business Card</title>
<link rel="stylesheet" href="https://fonts.googleapis.com/css2?family=Open+Sans:wght@400;600&display=swap">
<style>
  :root {
    --bg-top: #f4f4f4;
    --bg-bottom: #d9d9d9;
    --card: #fbfbfb;
    --ink: #555a5f;
    --ink-soft: #7a7f84;
    --brand-blue: #1f5fc4;
    --icon-blue: #2f6fd0;
  }
  * { box-sizing: border-box; margin: 0; padding: 0; }
  html, body { width: 1200px; height: 1200px; overflow: hidden; }
  body {
    background: linear-gradient(160deg, var(--bg-top), var(--bg-bottom));
    font-family: "Open Sans", Arial, sans-serif;
    display: flex; align-items: center; justify-content: center;
  }
  .business-card {
    position: relative;
    width: 980px; height: 560px;
    background: var(--card);
    box-shadow: 0 18px 40px rgba(0,0,0,0.12), 0 2px 6px rgba(0,0,0,0.08);
    color: var(--ink);
  }
  .person {
    position: absolute; left: 78px; top: 92px;
  }
  .person__name { font-size: 30px; line-height: 1.2; color: var(--ink); }
  .person__title { font-size: 28px; line-height: 1.2; color: var(--ink); margin-top: 2px; }
  .person__address { font-size: 22px; line-height: 1.35; color: var(--ink-soft); margin-top: 22px; }
  .brand {
    position: absolute; right: 70px; top: 150px;
    display: flex; align-items: center; gap: 18px;
  }
  .brand__mark { width: 34px; height: 34px; border-radius: 50%; background: var(--brand-blue); }
  .brand__name { font-size: 44px; font-weight: 600; color: var(--brand-blue); letter-spacing: 0.5px; }
  .contacts {
    position: absolute; left: 490px; top: 330px;
    list-style: none;
  }
  .contacts__item {
    display: flex; align-items: center; gap: 14px;
    font-size: 28px; line-height: 1.45; color: var(--ink);
  }
  .contacts__icon { width: 24px; height: 24px; flex: none; }
</style>
</head>
<body>
  <article class="business-card">
    <section class="person">
      <p class="person__name">name</p>
      <p class="person__title">xxxx xxxxx</p>
      <p class="person__address">Address : xxxxx xxxxxx<br>xxxxx xxx212, xxxxxxx</p>
    </section>

    <header class="brand">
      <span class="brand__mark" aria-hidden="true"></span>
      <span class="brand__name">Veltramo Consulting</span>
    </header>

    <ul class="contacts">
      <li class="contacts__item">
        <svg class="contacts__icon" viewBox="0 0 24 24" aria-hidden="true">
          <rect width="24" height="24" rx="5" fill="var(--icon-blue)"/>
          <path d="M8 5.5c-1.5 1-2 3 0 6.5s4.5 6 6.8 6.5l1.7-2-2.5-1.8-1.2 1.1c-1.3-.7-3-2.7-3.6-4l1.2-1.1L9.3 5z" fill="#fff"/>
        </svg>
        Mobile No. (TBA Later)
      </li>
      <li class="contacts__item">
        <svg class="contacts__icon" viewBox="0 0 24 24" aria-hidden="true">
          <rect width="24" height="24" rx="5" fill="var(--icon-blue)"/>
          <rect x="5" y="7" width="14" height="10" rx="1" fill="none" stroke="#fff" stroke-width="1.6"/>
          <path d="M5.5 7.5 12 12.5l6.5-5" fill="none" stroke="#fff" stroke-width="1.6"/>
        </svg>
        Email address (TBA Later)
      </li>
      <li class="contacts__item">
        <svg class="contacts__icon" viewBox="0 0 24 24" aria-hidden="true">
          <rect width="24" height="24" rx="5" fill="var(--icon-blue)"/>
          <circle cx="12" cy="12" r="6.5" fill="none" stroke="#fff" stroke-width="1.5"/>
          <ellipse cx="12" cy="12" rx="2.8" ry="6.5" fill="none" stroke="#fff" stroke-width="1.3"/>
          <path d="M5.5 12h13" stroke="#fff" stroke-width="1.3"/>
        </svg>
        Web address (TBA Later)
      </li>
    </ul>
  </article>
</body>
</html>
```